New design of skin care labels for a natural makeup company

Our company sells 100% natural makeup and also offers a small selection of skin care cosmetics which aren't fully organic but have natural ingredients where possible and made by hand in small batches.
We are an English company with Japanese influence in that our staff and company name are Japanese, we understand how natural cosmetics in Japan are a huge business as demanded by Japanese girls and we include some Japanese ingredients in our cosmetics though we are marketing and selling in the UK.
We want to re-design the labels for 6 lines of our skin care range of cosmetics. These would be a mix of toners, creams, gels & face wash. There are 3 label sizes HxW:
50 x 120 mm
65 x 130 mm
90 x 115 mm
Our products are priced between £10-£15 so not expensive but not drug store budget prices either. We want the new labels to portray:
More luxury than common every day counter products
More natural than chemically preserved, fragranced, artificial products
Show they are free from parabens/sulphates and possibly even announce hand made in England
They need to include the usual necessary information like ingredients, usage instructions, warnings, weights, contact details along with our logo which is trademarked so unfortunately can't be altered or recoloured as its a mono logo.
We are open to all your ideas but our instincts will probably favour something clean/clear looking rather than fussy - though not too minimalist. Our bottles are either clear or semi transparent so we might prefer a see-thru label to show off the product. However these are just ideas at the moment and we may decide against them after seeing your various designs.
Target Market(s)
Females who care more about what they put on their skin.
Industry/Entity Type
Cosmetics
Look and feel
Each slider illustrates characteristics of the customer's brand and the style your logo design should communicate.

```html
<!DOCTYPE html>
<html lang="en">
<head>
<meta charset="utf-8">
<title>Kohana skin care labels</title>
<link rel="stylesheet" href="https://fonts.googleapis.com/css2?family=Open+Sans:wght@700&family=Ubuntu:wght@400&display=swap">
<style>
  :root {
    --paper: #ffffff;
    --cream: #fbf8e1;
    --teal: #2ab0bc;
    --teal-light: #7fd4d8;
    --teal-pale: #a9e1e2;
    --teal-deep: #15808f;
    --teal-shadow: #0f6472;
    --text-cream: #fdf6d6;
    --white: #ffffff;
  }
  * { box-sizing: border-box; margin: 0; padding: 0; }
  html, body {
    width: 1200px; height: 900px; overflow: hidden;
    background: var(--paper);
  }
  .canvas { position: relative; width: 1200px; height: 900px; }

  .label {
    position: absolute;
    background: var(--cream);
    overflow: hidden;
  }
  .label-art { position: absolute; left: 0; top: 0; width: 100%; height: 100%; }

  .brand {
    position: absolute; left: 0; width: 100%;
    display: flex; flex-direction: column; align-items: center;
  }
  .brand-dot {
    display: block; border-radius: 50%;
    background: var(--white);
  }
  .brand-name {
    font-family: "Open Sans", sans-serif; font-weight: 700;
    color: var(--white); letter-spacing: 1px; line-height: 1;
  }

  .info-band {
    position: absolute; left: 0; width: 100%;
    background: linear-gradient(180deg, var(--teal-pale) 0%, var(--teal) 55%, var(--teal) 100%);
    color: var(--text-cream);
  }
  .info-title {
    font-family: "Ubuntu", sans-serif; font-weight: 400;
    text-align: center; letter-spacing: 0.5px; line-height: 1;
  }
  .info-copy {
    font-family: "Open Sans", sans-serif; font-weight: 700;
    color: var(--white); white-space: nowrap;
  }

  /* tall label */
  .label-tall { left: 218px; top: 204px; width: 202px; height: 405px; }
  .label-tall .brand { top: 48px; }
  .label-tall .brand-dot { width: 54px; height: 54px; margin-bottom: 14px; }
  .label-tall .brand-name { font-size: 25px; }
  .label-tall .info-band { top: 246px; height: 159px; padding: 12px 7px 0; }
  .label-tall .info-title { font-size: 25px; margin-bottom: 5px; }
  .label-tall .info-copy { font-size: 9.2px; line-height: 15px; letter-spacing: -0.15px; }

  /* wide label */
  .label-wide { left: 470px; top: 249px; width: 282px; height: 360px; }
  .label-wide .brand { top: 36px; }
  .label-wide .brand-dot { width: 60px; height: 60px; margin-bottom: 16px; }
  .label-wide .brand-name { font-size: 28px; }
  .label-wide .info-band { top: 250px; height: 110px; padding: 10px 10px 0; }
  .label-wide .info-title { font-size: 20px; margin-bottom: 6px; }
  .label-wide .info-copy { font-size: 9.2px; line-height: 15px; letter-spacing: -0.15px; }

  /* narrow label */
  .label-narrow { left: 803px; top: 234px; width: 157px; height: 375px; }
  .label-narrow .brand { top: 40px; }
  .label-narrow .brand-dot { width: 44px; height: 44px; margin-bottom: 12px; }
  .label-narrow .brand-name { font-size: 19px; }
  .label-narrow .info-band {
    top: 193px; height: 182px;
    writing-mode: vertical-rl;
    padding: 8px 10px 6px 0;
    background: linear-gradient(90deg, var(--teal) 0%, var(--teal) 45%, var(--teal-pale) 100%);
  }
  .label-narrow .info-title { font-size: 23px; text-align: left; margin-left: 10px; }
  .label-narrow .info-copy { font-size: 8.2px; line-height: 13px; letter-spacing: -0.1px; }
</style>
</head>
<body>
<main class="canvas">

  <!-- tall label -->
  <section class="label label-tall">
    <svg class="label-art" viewBox="0 0 202 405" aria-hidden="true">
      <defs>
        <linearGradient id="arrowTall" x1="0" y1="0" x2="0" y2="1">
          <stop offset="0" stop-color="#7fd4d8"/><stop offset="1" stop-color="#2ab0bc"/>
        </linearGradient>
      </defs>
      <rect x="0" y="0" width="202" height="24" fill="#2ab0bc"/>
      <polygon points="0,0 34,0 12,58 0,58" fill="#15808f"/>
      <polygon points="202,0 168,0 190,58 202,58" fill="#15808f"/>
      <polygon points="34,0 60,0 14,44" fill="#0f6472"/>
      <polygon points="168,0 142,0 188,44" fill="#0f6472"/>
      <path d="M10,28 H192 V160 L108,236 Q101,242 94,236 L10,160 Z" fill="#0f6472" opacity="0.25" transform="translate(2,4)"/>
      <path d="M10,28 H192 V160 L108,236 Q101,242 94,236 L10,160 Z" fill="url(#arrowTall)"/>
    </svg>
    <div class="brand"><span class="brand-dot"></span><span class="brand-name">KOHANA</span></div>
    <div class="info-band">
      <h2 class="info-title">YOUR TEXT</h2>
      <p class="info-copy">Lorem ipsum dolor sit amet, consectetur<br>elit, sed do eiusmod tempor incididunt u<br>dolore magna aliqua. Ut enim ad minim<br>quis nostrud exercitation ullamco laboris<br>aliquip ex ea commodo consequat.<br>Lorem ipsum dolor sit amet, consectetur<br>elit, sed do eiusmod tempor incididunt u</p>
    </div>
  </section>

  <!-- wide label -->
  <section class="label label-wide">
    <svg class="label-art" viewBox="0 0 282 360" aria-hidden="true">
      <defs>
        <linearGradient id="arrowWide" x1="0" y1="0" x2="0" y2="1">
          <stop offset="0" stop-color="#7fd4d8"/><stop offset="1" stop-color="#2ab0bc"/>
        </linearGradient>
      </defs>
      <polygon points="40,0 20,0 40,50" fill="#15808f"/>
      <polygon points="242,0 262,0 242,50" fill="#15808f"/>
      <polygon points="40,0 76,0 40,40" fill="#0f6472"/>
      <polygon points="242,0 206,0 242,40" fill="#0f6472"/>
      <path d="M40,6 H242 V118 L148,232 Q141,240 134,232 L40,118 Z" fill="#0f6472" opacity="0.25" transform="translate(2,4)"/>
      <path d="M40,6 H242 V118 L148,232 Q141,240 134,232 L40,118 Z" fill="url(#arrowWide)"/>
    </svg>
    <div class="brand"><span class="brand-dot"></span><span class="brand-name">KOHANA</span></div>
    <div class="info-band">
      <h2 class="info-title">YOUR TEXT</h2>
      <p class="info-copy">Lorem Ipsum is simply dummy text of the printing<br>and typesetting industry. Lorem Ipsum has been<br>the industry's standard dummy text ever since the<br>1500s,</p>
    </div>
  </section>

  <!-- narrow label -->
  <section class="label label-narrow">
    <svg class="label-art" viewBox="0 0 157 375" aria-hidden="true">
      <defs>
        <linearGradient id="arrowNarrow" x1="0" y1="0" x2="0" y2="1">
          <stop offset="0" stop-color="#7fd4d8"/><stop offset="1" stop-color="#2ab0bc"/>
        </linearGradient>
      </defs>
      <rect x="0" y="0" width="157" height="16" fill="#2ab0bc"/>
      <polygon points="0,0 26,0 8,46 0,46" fill="#15808f"/>
      <polygon points="157,0 131,0 149,46 157,46" fill="#15808f"/>
      <polygon points="26,0 46,0 10,34" fill="#0f6472"/>
      <polygon points="131,0 111,0 147,34" fill="#0f6472"/>
      <path d="M8,8 H149 V100 L84,182 Q78,189 72,182 L8,100 Z" fill="#0f6472" opacity="0.25" transform="translate(2,3)"/>
      <path d="M8,8 H149 V100 L84,182 Q78,189 72,182 L8,100 Z" fill="url(#arrowNarrow)"/>
    </svg>
    <div class="brand"><span class="brand-dot"></span><span class="brand-name">KOHANA</span></div>
    <div class="info-band">
      <h2 class="info-title">YOUR TEXT</h2>
      <p class="info-copy">Lorem ipsum dolor sit amet, consectetur<br>elit, sed do eiusmod tempor incididunt u<br>dolore magna aliqua. Ut enim ad minim<br>quis nostrud exercitation ullamco laboris<br>aliquip ex ea commodo consequat.</p>
    </div>
  </section>

</main>
</body>
</html>
```